Pharmacy ad

need 2 pharmacy ads for the phone book. one for Brookfield Pharmacy and one for Corvane Pharmacy. Dimensions for ad is 4.75in x 4.667 in. please see attached examples of ad uploaded as well logos of each pharmacy

```html
<!DOCTYPE html>
<html lang="en">
<head>
<meta charset="utf-8">
<title>Brookfield Pharmacy – Directory Ad</title>
<link rel="stylesheet" href="https://fonts.googleapis.com/css2?family=Montserrat:wght@300;400;500;600;700;800;900&family=Ubuntu:ital,wght@0,700;1,500&display=swap">
<style>
  :root {
    --navy: #1d1445;
    --green: #8cc63f;
    --green-light: #c7e3a0;
    --green-text: #6aab2e;
    --white: #ffffff;
    --photo-light: #e9ecef;
    --photo-mid: #c9b9ad;
    --ink: #1d1445;
  }
  * { margin: 0; padding: 0; box-sizing: border-box; }
  html, body { width: 1200px; height: 1200px; overflow: hidden; background: var(--white); }
  body { font-family: "Montserrat", sans-serif; color: var(--ink); }
  .ad { position: relative; width: 1200px; height: 1200px; background: var(--white); }
  .abs { position: absolute; }

  .brand-mark { left: 66px; top: 58px; width: 140px; height: 140px; border-radius: 50%; background: var(--green); }
  .brand-name { left: 232px; top: 88px; font-family: "Ubuntu", sans-serif; font-weight: 700; font-size: 45px; letter-spacing: -0.5px; color: var(--navy); white-space: nowrap; }
  .tagline { left: 270px; top: 156px; font-family: "Ubuntu", sans-serif; font-style: italic; font-weight: 500; font-size: 37px; color: var(--green-text); white-space: nowrap; }

  .hours { left: 835px; top: 62px; width: 300px; display: grid; grid-template-columns: 1fr 142px; column-gap: 10px; font-size: 25px; line-height: 38px; white-space: nowrap; }
  .hours .day { text-align: right; }
  .hours .time { font-weight: 700; text-align: left; }
  .hours .branch { grid-column: 1 / 3; text-align: right; font-size: 19px; line-height: 26px; }

  .photo { left: 0; top: 217px; width: 640px; height: 435px; background: linear-gradient(100deg, var(--photo-light) 0%, var(--photo-mid) 45%, var(--photo-light) 100%); }
  .panel { left: 0; top: 217px; }
  .features { left: 640px; top: 270px; list-style: none; color: var(--white); font-size: 29.5px; line-height: 35px; }
  .features li { position: relative; padding-left: 44px; margin-bottom: 10px; }
  .features svg { position: absolute; left: 0; top: 4px; }

  .offer-band { left: 0; top: 652px; width: 1200px; height: 199px; background: linear-gradient(90deg, var(--green) 0%, var(--green-light) 50%, var(--green) 100%); }
  .offer { top: 666px; width: 518px; height: 174px; background: var(--white); border-bottom-right-radius: 40px; border-top-left-radius: 12px; }
  .offer-senior { left: 65px; }
  .offer-student { left: 616px; }
  .offer .pct { position: absolute; left: 14px; top: -6px; font-weight: 900; font-size: 136px; letter-spacing: -6px; line-height: 150px; }
  .offer .label { position: absolute; font-weight: 800; font-size: 34px; line-height: 38px; }
  .offer .note { position: absolute; left: 0; width: 100%; bottom: 2px; text-align: center; font-size: 24px; }

  .services { left: 0; top: 850px; }
  .services-text { left: 64px; top: 864px; color: var(--white); font-size: 28.5px; letter-spacing: 0.4px; white-space: nowrap; }

  .address { font-size: 28px; line-height: 34px; }
  .address small { display: block; font-size: 22px; line-height: 26px; }
  .phone { font-weight: 800; font-size: 50px; letter-spacing: -0.5px; }
  .rule { left: 64px; top: 1014px; width: 708px; height: 2px; background: var(--navy); }

  .accepts { left: 830px; top: 876px; width: 310px; text-align: center; }
  .accept-title { font-size: 24px; font-weight: 500; letter-spacing: 8px; margin-bottom: 8px; }
  .partner { font-weight: 800; color: var(--navy); white-space: nowrap; }
  .insurer { font-size: 24px; line-height: 30px; }
  .cards { display: flex; justify-content: center; gap: 18px; margin-top: 24px; font-size: 21px; line-height: 28px; }
  .social { left: 842px; top: 1046px; }
</style>
</head>
<body>
<main class="ad">

  <div class="abs brand-mark" aria-hidden="true"></div>
  <h1 class="abs brand-name">BROOKFIELD PHARMACY</h1>
  <p class="abs tagline">We Care About Your Health</p>

  <div class="abs hours">
    <span class="day">Mon – Fri:</span><span class="time">10am-6pm</span>
    <span class="day">Sat:</span><span class="time">10am-5pm</span>
    <span class="day">Sun:</span><span class="time">10am-2pm</span>
    <span class="branch">(Marlow Street branch)</span>
  </div>

  <div class="abs photo" role="img" aria-label="Smiling pharmacist in a white coat standing in front of shelves of medicine"></div>
  <svg class="abs panel" width="1200" height="435" viewBox="0 0 1200 435" aria-hidden="true">
    <polygon points="614,0 1200,0 1200,435 500,435" fill="var(--navy)"/>
  </svg>

  <ul class="abs features">
    <li><svg width="32" height="30" viewBox="0 0 32 30"><path d="M2 16 L11 26 L30 3" fill="none" stroke="var(--green)" stroke-width="5" stroke-linecap="round" stroke-linejoin="round"/></svg>Certified Pharmacists</li>
    <li><svg width="32" height="30" viewBox="0 0 32 30"><path d="M2 16 L11 26 L30 3" fill="none" stroke="var(--green)" stroke-width="5" stroke-linecap="round" stroke-linejoin="round"/></svg>Affordable prices</li>
    <li><svg width="32" height="30" viewBox="0 0 32 30"><path d="M2 16 L11 26 L30 3" fill="none" stroke="var(--green)" stroke-width="5" stroke-linecap="round" stroke-linejoin="round"/></svg>Brand and Generic Medicines</li>
    <li><svg width="32" height="30" viewBox="0 0 32 30"><path d="M2 16 L11 26 L30 3" fill="none" stroke="var(--green)" stroke-width="5" stroke-linecap="round" stroke-linejoin="round"/></svg>Blood Pressure and<br>Glucose checks</li>
    <li><svg width="32" height="30" viewBox="0 0 32 30"><path d="M2 16 L11 26 L30 3" fill="none" stroke="var(--green)" stroke-width="5" stroke-linecap="round" stroke-linejoin="round"/></svg>Personal care and Beauty<br>Products</li>
    <li><svg width="32" height="30" viewBox="0 0 32 30"><path d="M2 16 L11 26 L30 3" fill="none" stroke="var(--green)" stroke-width="5" stroke-linecap="round" stroke-linejoin="round"/></svg>Injectables</li>
  </ul>

  <div class="abs offer-band"></div>
  <section class="abs offer offer-senior">
    <div class="pct">10%</div>
    <div class="label" style="left:305px; top:24px;">SENIOR<br>CITIZEN<br>DISCOUNT</div>
    <div class="note">For patients 60 years and over</div>
  </section>
  <section class="abs offer offer-student">
    <div class="pct">10%</div>
    <div class="label" style="left:311px; top:45px;">STUDENT<br>DISCOUNT</div>
    <div class="note">With valid ID card</div>
  </section>

  <svg class="abs services" width="690" height="60" viewBox="0 0 690 60" aria-hidden="true">
    <polygon points="0,0 689,0 674,60 0,60" fill="var(--navy)"/>
  </svg>
  <p class="abs services-text">SPECIAL ORDERS | DELIVERY SERVICE</p>

  <div class="abs address" style="left:64px; top:934px;">19 Marlow Street, Port Aldane<small>(opposite Elmridge Holiness Church)</small></div>
  <svg class="abs" style="left:492px; top:936px;" width="52" height="52" viewBox="0 0 52 52" aria-hidden="true">
    <circle cx="26" cy="26" r="23.5" fill="none" stroke="var(--green)" stroke-width="3"/>
    <path d="M18 14 c-3 2 -4 6 -1 12 c3 6 7 10 12 12 c4 1 6 -1 7 -3 l-5 -5 l-4 2 c-3 -2 -5 -5 -6 -8 l2 -4 z" fill="none" stroke="var(--green)" stroke-width="2.5" stroke-linejoin="round"/>
  </svg>
  <div class="abs phone" style="left:552px; top:930px;">555-0174</div>

  <div class="abs rule"></div>

  <div class="abs address" style="left:64px; top:1034px;">Pier Solana, Food Court,<br>Port Aldane</div>
  <svg class="abs" style="left:416px; top:1036px;" width="52" height="52" viewBox="0 0 52 52" aria-hidden="true">
    <circle cx="26" cy="26" r="23.5" fill="none" stroke="var(--green)" stroke-width="3"/>
    <path d="M18 14 c-3 2 -4 6 -1 12 c3 6 7 10 12 12 c4 1 6 -1 7 -3 l-5 -5 l-4 2 c-3 -2 -5 -5 -6 -8 l2 -4 z" fill="none" stroke="var(--green)" stroke-width="2.5" stroke-linejoin="round"/>
  </svg>
  <div class="abs phone" style="left:478px; top:1030px;">555-0177</div>

  <section class="abs accepts">
    <p class="accept-title">WE ACCEPT</p>
    <div class="partner insurer">Harbourline Insurances</div>
    <div class="cards">
      <span class="partner">SwiftPay</span>
      <span class="partner">CardOne</span>
      <span class="partner">Payvia</span>
    </div>
  </section>

  <div class="abs social">
    <div class="abs" style="left:0; top:0; width:66px; height:66px; background:var(--navy);" aria-hidden="true"></div>
    <div class="abs partner" style="left:88px; top:-4px; font-size:28px; font-weight:700;">Visit us on:</div>
    <div class="abs partner" style="left:86px; top:22px; font-size:44px;">Friendnet</div>
  </div>

</main>
</body>
</html>
```